Crestline Lending Group Business Cards

We are looking to revamp the current business cards each of our locations uses. We are a lending company that specializes in personal loans, title loans, and tax services. We have locations in New Mexico, Texas, and Oklahoma.

We would like a cleaner, sleeker look while still highlighting what we offer. Title Loans, Personal Loans & Tax Services. We also want to include our referral fee somewhere on the card. We would like to see an English option as well as a Spanish option for the cards.

PLEASE NOTE: Some business cards do not include the employee's name but just the store's location, while others will include both.

These are double-sided business cards, and we would like to see proof if possible. I have included proofs of our current business cards for you to review below, as well as our company logo. Feel free to get creative with the logo, etc! Colors should match the logo; however, you do not need to use all of our logo colors if you don't want to.

```html
<!DOCTYPE html>
<html lang="en">
<head>
<meta charset="utf-8">
<title>Crestline Lending Group Business Cards</title>
<link rel="stylesheet" href="https://fonts.googleapis.com/css2?family=Roboto:wght@300;400;500&display=swap">
<style>
  :root {
    --green: #10502f;
    --red: #c01f28;
    --ink: #222222;
    --muted: #4a4a4a;
    --paper: #ffffff;
    --backdrop: #ffffff;
  }
  * { box-sizing: border-box; margin: 0; padding: 0; }
  html, body {
    width: 1200px; height: 1000px; overflow: hidden;
    background: var(--backdrop);
    font-family: "Roboto", Arial, sans-serif;
  }
  .canvas { position: relative; width: 1200px; height: 1000px; }
  .card {
    position: absolute;
    background: var(--paper);
    box-shadow: 0 10px 40px rgba(0,0,0,0.12);
    overflow: hidden;
  }
  .card--front { left: 252px; top: 45px; width: 696px; height: 416px; }
  .card--back  { left: 251px; top: 533px; width: 697px; height: 419px; }

  .block { position: absolute; left: 103px; width: 169px; }
  .block--green { top: 0; height: 124px; background: var(--green); }
  .block--red { top: 285px; height: 131px; background: var(--red); }

  .brand-name {
    color: var(--green);
    font-weight: 500;
    text-align: center;
    line-height: 1.15;
  }
  .services {
    color: var(--red);
    font-weight: 400;
    text-transform: uppercase;
    text-align: center;
  }
  .card--front .brand-name {
    position: absolute; left: 88px; top: 178px; width: 199px;
    font-size: 22px;
  }
  .card--front .services {
    position: absolute; left: 88px; top: 237px; width: 199px;
    font-size: 9.5px; letter-spacing: 1.6px; line-height: 14px;
  }

  .person-icon { position: absolute; left: 369px; top: 92px; width: 29px; height: 35px; }
  .holder-name {
    position: absolute; left: 421px; top: 84px;
    font-size: 27px; font-weight: 500; color: var(--ink);
  }
  .holder-role {
    position: absolute; left: 421px; top: 116px;
    font-size: 16px; font-weight: 300; color: var(--muted);
  }

  .icon-bar { position: absolute; left: 370px; top: 196px; width: 29px; height: 133px; }
  .contact-group {
    position: absolute; left: 422px;
    font-size: 16px; font-weight: 300; color: var(--muted); line-height: 20.5px;
  }
  .contact-group--phone { top: 191px; }
  .contact-group--web { top: 240px; }
  .contact-group--place { top: 289px; }

  .card--back .brand-name {
    position: absolute; left: 0; right: 0; top: 150px;
    font-size: 38px;
  }
  .card--back .services {
    position: absolute; left: 0; right: 0;
    font-size: 11px; letter-spacing: 2px;
  }
  .services--en { top: 206px; }
  .services--es { top: 226px; }
  .referral {
    position: absolute; left: 0; right: 0; top: 292px;
    text-align: center; font-size: 13px; font-weight: 400; color: var(--muted);
    line-height: 18px;
  }
  .referral strong { color: var(--green); font-weight: 500; }
  .web-pill {
    position: absolute; left: 227px; top: 347px; width: 249px; height: 25px;
    border-radius: 13px; background: var(--green); color: #fff;
    font-size: 14px; font-weight: 500; letter-spacing: 4px;
    display: flex; align-items: center; justify-content: center;
  }
</style>
</head>
<body>
<div class="canvas">

  <section class="card card--front">
    <div class="block block--green"></div>
    <div class="brand-name">Crestline Lending Group</div>
    <div class="services">Title &amp; Personal Loans<br>Tax Services</div>
    <div class="block block--red"></div>

    <svg class="person-icon" viewBox="0 0 29 35" aria-hidden="true">
      <circle cx="14.5" cy="9" r="8.5" fill="var(--green)"/>
      <path d="M0 30 Q0 19 9 19 H20 Q29 19 29 30 V32 Q29 35 26 35 H3 Q0 35 0 32 Z" fill="var(--green)"/>
    </svg>
    <div class="holder-name">Daniel Reyes</div>
    <div class="holder-role">Branch Manager</div>

    <svg class="icon-bar" viewBox="0 0 29 133" aria-hidden="true">
      <rect x="0" y="0" width="29" height="133" rx="5" fill="var(--red)"/>
      <rect x="0" y="42" width="29" height="2" fill="#fff"/>
      <rect x="0" y="88" width="29" height="2" fill="#fff"/>
      <path d="M9 11 Q8 13 10 17 Q13 22 18 24 Q20 25 21 23 L21.5 21.5 L18.5 19.5 L17 21 Q14 19.5 12.5 16 L14 14.5 L12 11.5 Z" fill="#fff"/>
      <rect x="7" y="60" width="15" height="10" fill="#fff"/>
      <path d="M7 60 L14.5 66 L22 60 M7 70 L12 65 M22 70 L17 65" stroke="var(--red)" stroke-width="1" fill="none"/>
      <path d="M14.5 101 a5.5 5.5 0 0 1 5.5 5.5 c0 4 -5.5 9.5 -5.5 9.5 s-5.5 -5.5 -5.5 -9.5 a5.5 5.5 0 0 1 5.5 -5.5 z" fill="#fff"/>
      <circle cx="14.5" cy="106.5" r="2" fill="var(--red)"/>
    </svg>

    <div class="contact-group contact-group--phone">+000 123 456 7890<br>+000 123 456 7890</div>
    <div class="contact-group contact-group--web">yourgmail@name.com<br>www.websitename.com</div>
    <div class="contact-group contact-group--place">your street nmae here<br>New Yerk City, Zip - 000</div>
  </section>

  <section class="card card--back">
    <div class="brand-name">Crestline Lending Group</div>
    <div class="services services--en">Title Loans · Personal Loans · Tax Services</div>
    <div class="services services--es" lang="es">Préstamos de Título · Préstamos Personales · Impuestos</div>
    <div class="referral">
      Ask about our <strong>$50 referral fee</strong><br>
      <span lang="es">Pregunte por nuestra <strong>comisión de referido de $50</strong></span>
    </div>
    <div class="web-pill">www.websitename.com</div>
  </section>

</div>
</body>
</html>
```